Dovamel Nutrition Supplement Jar

Label for jar. White label on a brown bottle jar.
Conservative look, should look like medicine.
Main Side:
Oak Harbor Clinics (smaller size) (with logo)
DOVAMEL 10mg (large size)
Doctor Formulated
Developed in Clinical Practice
60 Capsules
(I prefer the single color white label with dark brown letters. Please stay close to that design)
(For the back side, please use the multicolor set up)
(The whole Label should be one color - white with dark brown letters)
Please visit my site for more inspiration and feel: www.velmorine.example
The product will be brown jar listed on this site.
Can you please provide one version without the text "Oak Harbor Clinics & Logo".
Thank you.

Target Market(s)

Women, 34-59 years old

Industry/Entity Type

Nutrition

Requirements
Should not have
• Multicolors, leaves,

```html
<!DOCTYPE html>
<html lang="en">
<head>
<meta charset="utf-8">
<title>Dovamel 10mg Label</title>
<link href="https://fonts.googleapis.com/css2?family=Rubik:wght@300;400;500;700&display=swap" rel="stylesheet">
<style>
  :root {
    --backdrop: #e8e8e8;
    --label-white: #fafafa;
    --ink-brown: #5a2c19;
    --rule-brown: #6b3420;
    --band-dark: #4f2412;
    --band-light: #8b4d31;
    --band-text: #f4ece6;
  }
  html, body {
    margin: 0;
    width: 1200px;
    height: 960px;
    overflow: hidden;
    background: var(--backdrop);
    font-family: "Rubik", sans-serif;
  }
  .label {
    position: absolute;
    left: 320px;
    top: 142px;
    width: 560px;
    height: 675px;
    background: var(--label-white);
    overflow: hidden;
  }
  .brand-mark {
    position: absolute;
    top: 78px;
    left: 0;
    width: 100%;
    display: flex;
    justify-content: center;
    align-items: center;
    gap: 8px;
    color: var(--ink-brown);
    font-size: 15px;
    font-weight: 400;
  }
  .brand-mark .dot {
    width: 14px;
    height: 14px;
    border-radius: 50%;
    background: var(--ink-brown);
  }
  .product-name {
    position: absolute;
    left: 70px;
    top: 262px;
    margin: 0;
    color: var(--ink-brown);
    font-size: 62px;
    line-height: 1;
    letter-spacing: 0.5px;
    white-space: nowrap;
  }
  .product-name .name { font-weight: 500; }
  .product-name .dose { font-weight: 300; }
  .title-rule {
    position: absolute;
    left: 75px;
    right: 0;
    top: 344px;
    height: 2px;
    background: var(--rule-brown);
  }
  .clinic-name {
    position: absolute;
    left: 71px;
    top: 357px;
    color: var(--ink-brown);
    font-size: 27px;
    font-weight: 300;
  }
  .claim {
    position: absolute;
    left: 22px;
    top: 545px;
    color: var(--ink-brown);
    font-size: 26px;
    font-weight: 700;
    letter-spacing: 0.3px;
  }
  .band {
    position: absolute;
    left: 0;
    top: 0;
    width: 560px;
    height: 675px;
  }
  .practice-line {
    position: absolute;
    left: 47px;
    top: 628px;
    color: var(--band-text);
    font-size: 20px;
    font-weight: 300;
    letter-spacing: 0.3px;
  }
  .count {
    position: absolute;
    left: 446px;
    top: 593px;
    display: flex;
    align-items: flex-start;
    gap: 6px;
    color: var(--band-text);
  }
  .count .number {
    font-size: 34px;
    font-weight: 700;
    line-height: 1;
  }
  .count .unit {
    font-size: 11px;
    font-weight: 300;
  }
</style>
</head>
<body>
  <div class="label">
    <svg class="band" viewBox="0 0 560 675" aria-hidden="true">
      <defs>
        <linearGradient id="bandFill" x1="0" y1="0" x2="1" y2="0">
          <stop offset="0" stop-color="var(--band-dark)"/>
          <stop offset="1" stop-color="var(--band-light)"/>
        </linearGradient>
      </defs>
      <path d="M0 600 L310 600 C390 600 410 532 490 530 L560 530 L560 675 L0 675 Z" fill="url(#bandFill)"/>
    </svg>

    <div class="brand-mark"><span class="dot"></span><span>Oak Harbor Clinics</span></div>

    <h1 class="product-name"><span class="name">DOVAMEL</span> <span class="dose">10mg</span></h1>
    <div class="title-rule"></div>
    <div class="clinic-name">Oak Harbor Clinics</div>

    <div class="claim">DOCTOR FORMULATED</div>
    <div class="practice-line">DEVELOPED IN CLINICAL PRACTICE</div>

    <div class="count">
      <svg width="26" height="50" viewBox="0 0 26 50" aria-hidden="true">
        <rect x="2" y="2" width="22" height="46" rx="11" fill="none" stroke="var(--band-text)" stroke-width="2.5"/>
        <path d="M2 25 L2 13 A11 11 0 0 1 24 13 L24 25 Z" fill="var(--band-text)"/>
      </svg>
      <div>
        <div class="number">60</div>
        <div class="unit">Capsules</div>
      </div>
    </div>
  </div>
</body>
</html>
```